wedding DJ & Lighting entertainment

We are a DJ and Lighting production company. We specialize mainly in wedding entertainment. I've attached my old postcard in the image folder, however, i would like something new and updated. You can use the same bullet points from the front page, but i would like to have a cleaner look on the front. I'd like to have one large image on the front side and smaller images on the back side. I'd also like to have some text below the logo. I'd like it to say DJ * Lighting * Audio/Visual. I'd also like to have the phrase "Celebrate with Style"

Target Market(s)

weddings, private events, women

Industry/Entity Type

It Company

Font styles to use
Sans Serif
Script

Requirements
Must have
• look elegant, sophisticated. Must have my new logo! My logo is attached as one of the files. It's a headphone logo.

```html
<!DOCTYPE html>
<html lang="en">
<head>
<meta charset="utf-8">
<title>Echoline Productions – Postcard</title>
<link rel="stylesheet" href="https://fonts.googleapis.com/css2?family=Great+Vibes&family=Raleway:wght@400;500;600&display=swap">
<style>
  :root {
    --canvas: #e9e8ea;
    --brand-red: #e0262d;
    --ink: #333036;
    --white: #ffffff;
    --plum-deep: #2a0f3a;
    --plum: #5b2479;
    --violet: #8a45b8;
    --magenta: #c2186b;
    --pink-soft: #e9c9e6;
    --card-shadow: 0 3px 10px rgba(0,0,0,.25);
  }
  * { box-sizing: border-box; margin: 0; padding: 0; }
  html, body { width: 800px; height: 1200px; overflow: hidden; }
  body {
    background: var(--canvas);
    font-family: "Raleway", Arial, sans-serif;
    position: relative;
  }

  /* ---------- Front side ---------- */
  .card { position: absolute; left: 32px; width: 741px; box-shadow: var(--card-shadow); overflow: hidden; }
  .card--front { top: 14px; height: 574px; }
  .front-photo {
    position: absolute; inset: 0;
    background:
      radial-gradient(ellipse at 28% 45%, #f1e6ee 0%, #b88bb9 16%, transparent 38%),
      radial-gradient(ellipse at 75% 20%, #a96bd0 0%, transparent 55%),
      linear-gradient(120deg, var(--plum-deep) 0%, var(--plum) 40%, var(--violet) 70%, #3a1650 100%);
  }
  .front-content {
    position: absolute; left: 370px; right: 20px; top: 44px;
    color: var(--white); text-align: center;
  }
  .brand { display: flex; align-items: center; justify-content: center; gap: 12px; }
  .brand__dot { width: 34px; height: 34px; border-radius: 50%; background: var(--brand-red); }
  .brand__name {
    font-family: "Raleway", Arial, sans-serif; font-weight: 600;
    color: var(--brand-red); font-size: 40px; letter-spacing: 1px; line-height: 1;
  }
  .brand__sub {
    font-family: "Raleway", Arial, sans-serif; font-weight: 600;
    color: var(--brand-red); font-size: 14px; letter-spacing: 5px; margin-top: 6px;
  }
  .services-line { font-size: 20px; font-weight: 500; margin-top: 26px; letter-spacing: .5px; }
  .headline {
    font-family: "Great Vibes", cursive; font-weight: 400;
    font-size: 60px; margin-top: 22px; line-height: 1; text-align: left; padding-left: 10px;
  }
  .feature-list {
    list-style: none; text-align: left; margin: 34px 0 0 40px;
    font-size: 19px; font-weight: 500;
  }
  .feature-list li { margin-bottom: 16px; }
  .feature-list li::before { content: "•"; color: var(--pink-soft); margin-right: 10px; }

  /* ---------- Back side ---------- */
  .card--back { top: 612px; height: 560px; background: var(--white); }
  .photo { position: absolute; border: 3px solid var(--white); outline: 1px solid #ccc; }
  .photo--venue-blue { left: 20px; top: 22px; width: 186px; height: 160px;
    background: radial-gradient(circle at 50% 55%, #b38cf0 0%, #4a2a9c 45%, #1e1447 100%); }
  .photo--ballroom { left: 218px; top: 22px; width: 268px; height: 160px;
    background: linear-gradient(180deg, #2a1d6e 0%, #6c5bd6 45%, #c9c3f3 70%, #40308f 100%); }
  .photo--crowd-bw { left: 498px; top: 22px; width: 223px; height: 160px;
    background: linear-gradient(160deg, #f1f1f1 0%, #8c8c8c 40%, #222 100%); }
  .photo--first-dance { left: 20px; top: 194px; width: 466px; height: 176px;
    background: radial-gradient(ellipse at 40% 60%, #f4ede5 0%, #b59a7a 18%, transparent 40%),
                linear-gradient(120deg, #3a1a55 0%, #6b3a8a 45%, #b08a4a 100%); }
  .photo--party-pink { left: 498px; top: 194px; width: 223px; height: 176px;
    background: linear-gradient(150deg, #f7b6d6 0%, #d9407f 45%, #4a1030 100%); }
  .photo--dance-floor { left: 218px; top: 382px; width: 268px; height: 150px;
    background: linear-gradient(170deg, #2b1d46 0%, #8d5b6b 45%, #d9a77c 70%, #2a1a2e 100%); }
  .photo--hands-bw { left: 498px; top: 382px; width: 223px; height: 150px;
    background: linear-gradient(160deg, #e6e6e6 0%, #7a7a7a 45%, #161616 100%); }

  .swoosh { position: absolute; left: 0; top: 330px; width: 741px; height: 230px; }

  .back-brand { position: absolute; left: 28px; top: 402px; width: 180px; text-align: center; }
  .back-brand .brand { gap: 8px; }
  .back-brand .brand__dot { width: 20px; height: 20px; }
  .back-brand .brand__name { font-size: 24px; }
  .back-brand .brand__sub { font-size: 9px; letter-spacing: 3px; margin-top: 4px; }

  .contact { position: absolute; left: 30px; top: 500px; display: flex; align-items: center; gap: 8px;
    color: var(--ink); font-size: 17px; font-weight: 600; }
  .contact svg { width: 16px; height: 16px; }
  .web { position: absolute; left: 236px; top: 538px; font-size: 9px; color: var(--ink); line-height: 1.3; }
</style>
</head>
<body>

<section class="card card--front">
  <div class="front-photo" role="img" aria-label="Bride and groom sharing a first dance in a ballroom washed with purple uplighting"></div>
  <div class="front-content">
    <div class="brand">
      <span class="brand__dot"></span>
      <span class="brand__name">echoline</span>
    </div>
    <div class="brand__sub">PRODUCTIONS</div>
    <p class="services-line">DJ • Lighting • Audio/Visual</p>
    <h1 class="headline">Celebrate with Style</h1>
    <ul class="feature-list">
      <li>DJ and Emcee Entertainment</li>
      <li>Customized Lighting Decor</li>
      <li>Event Hosting and Coordination</li>
      <li>Helpful Planning Tools</li>
      <li>Personalized Service</li>
    </ul>
  </div>
</section>

<section class="card card--back">
  <div class="photo photo--venue-blue" role="img" aria-label="Reception table with centerpiece under blue and violet lighting"></div>
  <div class="photo photo--ballroom" role="img" aria-label="Wide view of a ballroom with lavender uplighting and monogram projection"></div>
  <div class="photo photo--crowd-bw" role="img" aria-label="Black and white shot of guests dancing with raised hands"></div>
  <div class="photo photo--first-dance" role="img" aria-label="Couple dancing in a lit reception hall"></div>
  <div class="photo photo--party-pink" role="img" aria-label="Guests celebrating on a pink-lit dance floor"></div>

  <svg class="swoosh" viewBox="0 0 741 230" preserveAspectRatio="none" aria-hidden="true">
    <path d="M0 60 Q 300 10 741 90 L741 230 L0 230 Z" fill="#ffffff"/>
    <path d="M0 60 Q 300 10 741 90" fill="none" stroke="#c2186b" stroke-width="6"/>
    <path d="M0 70 Q 300 22 741 100" fill="none" stroke="#8a45b8" stroke-width="3"/>
  </svg>

  <div class="photo photo--dance-floor" role="img" aria-label="Crowded dance floor with warm stage lights"></div>
  <div class="photo photo--hands-bw" role="img" aria-label="Black and white photo of a lively party crowd"></div>

  <div class="back-brand">
    <div class="brand">
      <span class="brand__dot"></span>
      <span class="brand__name">echoline</span>
    </div>
    <div class="brand__sub">PRODUCTIONS</div>
  </div>

  <div class="contact">
    <svg viewBox="0 0 24 24" aria-hidden="true"><path fill="#333036" d="M6.6 10.8a15 15 0 006.6 6.6l2.2-2.2c.3-.3.7-.4 1-.2 1.1.4 2.3.6 3.6.6.6 0 1 .4 1 1V20c0 .6-.4 1-1 1A17 17 0 013 4c0-.6.4-1 1-1h3.5c.6 0 1 .4 1 1 0 1.3.2 2.5.6 3.6.1.3 0 .7-.2 1z"/></svg>
    <span>555-014-2290</span>
  </div>
  <div class="web">echolinepros.com<br>events@echolinepros.com</div>
</section>

</body>
</html>
```